Business card design for BrandVexa
BrandVexa
Project: Business card design for BrandVexa
Business card design for BrandVexa - Printing
Creative Brief
Professional
Dalton Wexford
Maplecrest, Ontario, Canada
dalton@brandvexa.example
www.brandvexa.example
Possibly a dark background with nice effects. I am open to layer effect changes of my logo "BV". I will be changing my website banner in the future as well to make everything uniform.
Logo and web address logo can be downloaded here: https://www.filedrop.example/s/q8271n904tbpe3x/BV%20logo%20red%20and%20black.psd
brandvexa brandvexa
I like the bak of draft 44
I believe the"BV" box in the logo should be removed on the front of the cards. It just doesn't look right with the arched themed designs. I do like just the "BV" on the back of the card with url. I was hoping for more effects in the colour rather than just solid. Less red and more grey fading into lighter greys. Hopes this makes sense. Thanks for your hard work!

```html
<!DOCTYPE html>
<html lang="en">
<head>
<meta charset="utf-8">
<title>BrandVexa Business Card</title>
<link rel="stylesheet" href="https://fonts.googleapis.com/css2?family=Open+Sans:wght@400;600;700&display=swap">
<style>
  :root {
    --bg: #e4e2de;
    --card-dark: #2b2b2d;
    --card-mid: #47474a;
    --card-light: #5e5e62;
    --text-main: #ffffff;
    --text-soft: #c9c9cc;
    --text-faint: #8d8d92;
    --chip: #77777c;
  }
  * { margin: 0; padding: 0; box-sizing: border-box; }
  html, body { width: 1200px; height: 1023px; overflow: hidden; }
  body {
    background: var(--bg);
    font-family: "Open Sans", Arial, sans-serif;
    position: relative;
  }
  .card {
    position: absolute;
    top: 180px;
    width: 380px;
    height: 664px;
    border-radius: 6px;
    background: linear-gradient(160deg, var(--card-light) 0%, var(--card-mid) 35%, var(--card-dark) 100%);
    box-shadow: 0 18px 40px rgba(0,0,0,0.25);
    color: var(--text-main);
    overflow: hidden;
  }
  .card--front { left: 170px; }
  .card--back { left: 650px; }

  .brand-name {
    font-weight: 600;
    letter-spacing: 2px;
    color: var(--text-main);
    text-transform: uppercase;
    white-space: nowrap;
  }
  .card--front .brand-name {
    position: absolute;
    top: 110px;
    width: 100%;
    text-align: center;
    font-size: 34px;
  }
  .person {
    position: absolute;
    top: 200px;
    width: 100%;
    text-align: center;
  }
  .person-name { font-size: 30px; font-weight: 700; }
  .person-role { font-size: 18px; color: var(--text-soft); margin-top: 4px; }

  .contact-list {
    position: absolute;
    top: 320px;
    left: 70px;
    right: 20px;
    list-style: none;
  }
  .contact-item {
    display: flex;
    align-items: center;
    gap: 14px;
    font-size: 17px;
    color: var(--text-soft);
    height: 30px;
    white-space: nowrap;
  }
  .contact-icon { width: 18px; height: 18px; flex: none; }
  .contact-icon--blank { visibility: hidden; }

  .social-row {
    position: absolute;
    top: 560px;
    left: 70px;
    display: flex;
    gap: 10px;
  }
  .social-chip { width: 24px; height: 24px; border-radius: 3px; background: var(--chip); }

  .card--back .brand-name {
    position: absolute;
    top: 300px;
    width: 100%;
    text-align: center;
    font-size: 40px;
  }
  .back-url {
    position: absolute;
    left: 22px;
    bottom: 200px;
    transform: rotate(-90deg);
    transform-origin: left bottom;
    font-size: 12px;
    color: var(--text-faint);
    letter-spacing: 1px;
    white-space: nowrap;
  }
</style>
</head>
<body>
  <section class="card card--front" aria-label="Front of business card">
    <div class="brand-name">BrandVexa</div>
    <div class="person">
      <div class="person-name">Dalton Wexford</div>
      <div class="person-role">Manager</div>
    </div>
    <ul class="contact-list">
      <li class="contact-item">
        <svg class="contact-icon" viewBox="0 0 18 18"><path d="M1 9 L9 2 L17 9 H14.5 V16 H10.5 V11.5 H7.5 V16 H3.5 V9 Z" fill="#ffffff"/></svg>
        Maplecrest, Ontario, Canada
      </li>
      <li class="contact-item">
        <svg class="contact-icon contact-icon--blank" viewBox="0 0 18 18"></svg>
        1 800 555 0142
      </li>
      <li class="contact-item">
        <svg class="contact-icon" viewBox="0 0 18 18"><path d="M4 2 L7 2 L8 6 L6 7.5 C7 10 8 11 10.5 12 L12 10 L16 11 L16 14 C16 15 15 16 14 16 C7.5 16 2 10.5 2 4 C2 3 3 2 4 2 Z" fill="#ffffff"/></svg>
        780 555 0118
      </li>
      <li class="contact-item">
        <svg class="contact-icon" viewBox="0 0 18 18"><rect x="5" y="1" width="8" height="16" rx="1.5" fill="#ffffff"/><rect x="6.5" y="3" width="5" height="10" fill="#47474a"/></svg>
        780 555 0172
      </li>
      <li class="contact-item">
        <svg class="contact-icon" viewBox="0 0 18 18"><rect x="2" y="7" width="14" height="8" rx="1" fill="#ffffff"/><rect x="5" y="2" width="8" height="6" fill="#ffffff"/><rect x="6" y="3" width="6" height="4" fill="#47474a"/></svg>
        780 555 0188
      </li>
      <li class="contact-item">
        <svg class="contact-icon" viewBox="0 0 18 18"><rect x="1.5" y="4" width="15" height="10" rx="1" fill="none" stroke="#ffffff" stroke-width="1.5"/><path d="M2 4.5 L9 10 L16 4.5" fill="none" stroke="#ffffff" stroke-width="1.5"/></svg>
        dalton@brandvexa.example
      </li>
    </ul>
    <div class="social-row" aria-label="Social profiles">
      <span class="social-chip"></span>
      <span class="social-chip"></span>
      <span class="social-chip"></span>
    </div>
  </section>

  <section class="card card--back" aria-label="Back of business card">
    <div class="brand-name">BrandVexa</div>
    <div class="back-url">www.brandvexa.example</div>
  </section>
</body>
</html>
```